VoltNest EV Charger Installation

We are an electrical contractor "Brannock Electric" http://brannockelectricservices.example.

New site is for a division we are creating. http://voltnestelectric.example/ is registered on Google domains.
Company is registered as VoltNest LLC.
VoltNest is something we are trying out to see if we can find a niche installing EV chargers and EV Charger outlets in existing homes and businesses. Looking to work it as a division off from Brannock Electric short term and if successful it would become a stand alone business. Often times this requires additional work to meet code. Work such as adding smoke & carbon monoxide detectors, new electrical panels and upgrading the electrical Main Service Meter system.
Will need to coordinate this site with our current Brannock Electric website. Not sure how this can work. We like the look of our current Brannock Electric Wordpress site, but it is dated and broken, in need of a rebuild or repair as well.
Need a website as a landing point for Google Maps inquiries and possibly as a way to drive customers to call for our services. Need to be mindful that we want to avoid confusion with people looking for EV charger Stations to drive and plug in their cars. We are a contractor not a place to plug in! The name may be problematic in this sense.
Looking for a site that coordinates style & color with the provided VoltNest logo. Would like to have a contact / inquiry page with a captcha or similar tool to weed out spam. need to integrate google maps and similar tools to measure marketing, assist in lead generation, etc.
Have Logo artwork. Not sure what format is best to upload.

Target Market(s)

People with electric cars, business owners and homeowners.

Industry/Entity Type

Electrical Contractor- Residential & Light Commercial (mostly residential)

Coding

Coded - Design and coding required

Number of Pages Required

3 page

Requirements
Must have
• Landing Page/about us , Contact Us/ inquiry Page with a quality captcha filter, Job Gallery- we don't have many pics yet. Google pointers /tools. Open to suggestions here! Mobile Phone/ Tablet friendly is important. I listed coded design but not quite sure what that means.
Nice to have
• Similar to the Brannock Electric site style a possibility, but open to suggestions. Possibly have something that shows the business is connected to Brannock Electric? ..."A division of Brannock Electric" with logo/link to site?

```html
<!DOCTYPE html>
<html lang="en">
<head>
<meta charset="utf-8">
<title>VoltNest EV Charger Installation</title>
<link href="https://fonts.googleapis.com/css2?family=Roboto+Condensed:wght@400;500;700&family=Roboto:wght@400;500&display=swap" rel="stylesheet">
<style>
:root{
  --green:#7cc242;
  --green-dark:#1f5a17;
  --green-deep:#0f4a0c;
  --ink:#1b1b1b;
  --text:#4a4a4a;
  --muted:#6d6d6d;
  --panel:#f1f1f1;
  --line:#d9d9d9;
  --footer:#222222;
  --white:#ffffff;
}
*{box-sizing:border-box;margin:0;padding:0}
html,body{width:1200px;height:3349px;overflow:hidden}
body{position:relative;background:var(--white);font-family:"Roboto Condensed",sans-serif;color:var(--ink)}
.abs{position:absolute}
a{color:inherit;text-decoration:none}

/* header */
.site-header{left:0;top:0;width:1200px;height:74px;background:var(--white)}
.brand{display:flex;align-items:center;gap:10px}
.brand-mark{width:36px;height:36px;border-radius:50%;background:var(--green)}
.brand-name{font-family:"Roboto Condensed",sans-serif;font-weight:700;font-size:28px;color:var(--ink);letter-spacing:.5px}
.brand-tag{font-size:8px;color:var(--ink);letter-spacing:.5px;font-style:normal}
.main-nav{top:30px;left:612px;display:flex;gap:26px;font-size:13px;font-weight:500;color:var(--ink)}
.call{left:914px;top:16px;display:flex;align-items:center;gap:8px}
.call-icon{width:38px;height:38px;border-radius:50%;border:2px solid #dceccf;background:var(--green);display:flex;align-items:center;justify-content:center}
.call-label{font-size:11px;color:var(--green)}
.call-number{font-size:13px;font-weight:700}

/* hero */
.hero-left{left:0;top:74px;width:541px;height:424px;background:linear-gradient(90deg,#2a2520 0%,#4a3f36 55%,#6a5e52 100%)}
.hero-right{left:541px;top:74px;width:659px;height:424px;background:linear-gradient(110deg,#6b7378 0%,#8f979c 45%,#5c6468 100%)}
.hero-title{left:150px;top:170px;font-size:46px;font-weight:700;line-height:52px;color:var(--white)}
.hero-sub{left:150px;top:296px;font-size:14px;font-weight:700;color:var(--white)}
.hero-list{left:150px;top:328px;width:350px;list-style:none;color:var(--white);font-size:11.5px;line-height:16px}
.hero-list li{position:relative;padding-left:28px;margin-bottom:14px}
.hero-list li::before{content:"";position:absolute;left:0;top:0;width:18px;height:18px;border-radius:50%;background:var(--green)}

/* intro */
.intro-bg{left:12px;top:498px;width:1188px;height:589px;background:var(--panel)}
.intro-title{left:0;top:594px;width:1200px;text-align:center;font-size:34px;font-weight:700}
.intro-photo{left:177px;top:685px;width:322px;height:402px;background:linear-gradient(160deg,#c9ccd2 0%,#3e5a8c 55%,#2a3f74 100%)}
.intro-photo-top{left:270px;top:660px;width:100px;height:40px;border-radius:50px 50px 0 0;background:#ececec}
.intro-copy{left:569px;top:708px;width:330px}
.intro-copy h3{font-size:20px;font-weight:700;margin-bottom:16px}
.rule{width:80px;height:3px;background:var(--green)}
.intro-copy .lead{font-size:13px;font-weight:700;margin:20px 0 14px}
.intro-copy p{font-size:12.5px;line-height:22px;color:var(--text)}
.proof{left:569px;top:934px;width:300px;height:50px;border-top:1px solid var(--line);border-bottom:1px solid var(--line);display:flex;align-items:center}
.partner{font-size:19px;font-weight:700;color:#c8202a;width:165px}
.proof-sep{width:1px;height:40px;background:var(--line);margin-right:22px}
.stat{font-size:36px;font-weight:700;color:var(--green);margin-right:18px}
.stat-label{font-size:13px;font-weight:500;line-height:16px}

/* consultation */
.consult-title{left:0;top:1165px;width:1200px;text-align:center;font-family:"Roboto",sans-serif;font-size:21px;font-weight:500;line-height:30px;letter-spacing:.3px}
.consult-rule{left:559px;top:1232px;width:82px;height:3px;background:var(--green)}
.step{width:200px;text-align:center;font-family:"Roboto",sans-serif;font-size:11.5px;line-height:15px;color:var(--muted)}
.step-icon{width:44px;height:44px;margin:0 auto 10px;border-radius:50%;border:1px solid var(--line);background:var(--white);display:flex;align-items:center;justify-content:center}
.hub-name{font-size:30px;font-weight:700;color:var(--ink)}

/* cost */
.cost-left{left:0;top:1640px;width:632px;height:479px;background:linear-gradient(120deg,#2f6a24 0%,#21561a 50%,#1a4a14 100%)}
.cost-photo{left:632px;top:1640px;width:568px;height:384px;background:linear-gradient(100deg,#d6d8da 0%,#9fa3a6 40%,#2a2c2e 60%,#b9bcbf 100%)}
.cost-copy{left:157px;top:1735px;width:345px;color:var(--white)}
.cost-copy h2{font-size:20px;font-weight:700;margin-bottom:14px}
.cost-copy .rule{width:80px;height:2px;background:var(--white)}
.cost-copy p{font-size:12.5px;line-height:22px;margin-top:34px}
.price{display:flex;align-items:center;gap:14px;margin-top:20px;font-size:13px;font-weight:700;line-height:21px}
.price-icon{width:40px;height:40px;border-radius:50%;border:1px solid rgba(255,255,255,.7);display:flex;align-items:center;justify-content:center;font-size:20px;font-weight:400}
.cost-copy p.after{margin-top:18px}
.permit{left:682px;top:2068px;width:400px;font-size:14px;font-weight:700;line-height:24px;letter-spacing:.3px}

/* projects */
.projects-bg{left:12px;top:2220px;width:1188px;height:611px;background:var(--panel)}
.projects-title{left:0;top:2282px;width:1200px;text-align:center;font-family:"Roboto",sans-serif;font-size:21px;font-weight:500}
.projects-rule{left:569px;top:2323px;width:62px;height:3px;background:var(--green)}
.project{top:2354px;width:229px;height:333px}
.p1{left:142px;background:linear-gradient(170deg,#ded8cc 0%,#b9ad99 60%,#8f867a 100%)}
.p2{left:371px;background:linear-gradient(180deg,#b6c2a4 0%,#8f9d7e 100%)}
.p2-overlay{left:371px;top:2521px;width:229px;height:166px;background:var(--green-deep);color:var(--white);text-align:center;padding:44px 20px 0}
.p2-overlay h4{font-size:12.5px;font-weight:700;margin-bottom:12px;letter-spacing:.3px}
.p2-overlay p{font-family:"Roboto",sans-serif;font-size:10.5px;line-height:15px;color:#d5e4cf}
.p3{left:600px;background:linear-gradient(180deg,#e8e8e6 0%,#cfd1cf 100%)}
.p4{left:829px;background:linear-gradient(180deg,#3d5a2e 0%,#8a6a4c 50%,#7a5b3c 100%)}
.arrow{top:2493px;width:57px;height:57px;border-radius:50%;background:var(--white);border:1px solid var(--line);display:flex;align-items:center;justify-content:center}
.btn-outline{left:519px;top:2731px;width:162px;height:48px;border:1px solid #9fbf8b;background:var(--white);display:flex;align-items:center;justify-content:center;font-size:14px;font-weight:700;letter-spacing:.3px}

/* cta */
.cta{left:0;top:2831px;width:1200px;height:325px;background:linear-gradient(90deg,#114a0d 0%,#1f5a17 40%,#6f8766 75%,#b9c0b6 100%)}
.cta-title{left:145px;top:2924px;width:700px;font-size:33px;font-weight:700;line-height:47px;color:var(--white)}
.btn-green{left:141px;top:3062px;width:230px;height:44px;background:var(--green);color:var(--white);display:flex;align-items:center;justify-content:center;font-size:14px;font-weight:700;letter-spacing:.3px}

/* footer */
.site-footer{left:0;top:3156px;width:1200px;height:193px;background:var(--footer);color:var(--white)}
.footer-brand .brand-name{color:var(--white)}
.footer-brand .brand-tag{color:var(--white)}
.footer-nav{left:548px;top:3203px;list-style:none;font-size:12.5px;line-height:28px}
.footer-contact{left:731px;top:3206px;list-style:none;font-family:"Roboto",sans-serif;font-size:10.5px;color:#cfcfcf}
.footer-contact li{display:flex;gap:8px;margin-bottom:10px;line-height:13px}
.follow{left:965px;top:3206px;font-family:"Roboto",sans-serif;font-size:10.5px;color:#cfcfcf}
.socials{left:960px;top:3234px;display:flex;gap:14px}
.social{width:16px;height:16px;border-radius:50%;border:1.5px solid var(--white)}
.copyright{left:145px;top:3313px;font-size:12px}
</style>
</head>
<body>

<header class="abs site-header">
  <a class="abs brand" href="#" style="left:143px;top:12px">
    <span class="brand-mark"></span>
    <span><span class="brand-name">VoltNest</span><br><span class="brand-tag">EV CHARGER INSTALLATION</span></span>
  </a>
  <nav class="abs main-nav"><a href="#">HOME</a><a href="#">JOB GALLERY</a><a href="#">CONTACT US</a></nav>
  <div class="abs call">
    <span class="call-icon"><svg width="16" height="16" viewBox="0 0 24 24"><path fill="#fff" d="M6.6 10.8a15 15 0 0 0 6.6 6.6l2.2-2.2a1 1 0 0 1 1-.25 11.4 11.4 0 0 0 3.6.57 1 1 0 0 1 1 1V20a1 1 0 0 1-1 1A17 17 0 0 1 3 4a1 1 0 0 1 1-1h3.5a1 1 0 0 1 1 1c0 1.25.2 2.45.57 3.57a1 1 0 0 1-.25 1z"/></svg></span>
    <span><span class="call-label">Give Us a Call</span><br><span class="call-number">555 - 014 - 2290</span></span>
  </div>
</header>

<section>
  <div class="abs hero-left" role="img" aria-label="House exterior with windows at dusk"></div>
  <div class="abs hero-right" role="img" aria-label="Green wall-mounted EV charger with coiled cable"></div>
  <h1 class="abs hero-title">Adaptable and<br>Eco-Friendly Option</h1>
  <p class="abs hero-sub">EV CHARGERS SYSTEM CAPABLE OF:</p>
  <ul class="abs hero-list">
    <li>providing fast and convenient charging for electric vehicles.</li>
    <li>delivering different levels of power output, which can impact the speed of charging.</li>
    <li>smart features that optimize and monitor the charging process for greater control.</li>
  </ul>
</section>

<section>
  <div class="abs intro-bg"></div>
  <h2 class="abs intro-title">Need An Electric Car Charger?</h2>
  <div class="abs intro-photo" role="img" aria-label="Electricians in hard hats assembling an EV charger"></div>
  <div class="abs intro-copy">
    <h3>ELECTRIC VEHICLES (EVS) ARE HERE</h3>
    <div class="rule"></div>
    <p class="lead">Let VoltNest help you get powered up!</p>
    <p>EV charger installation is a relatively simple process, but it's important to hire a qualified electrician. VoltNest is a division of Brannock Electric, a licensed and insured electrical contractor. We are committed to providing our customers with a quality, code approved installation.</p>
  </div>
  <div class="abs proof">
    <span class="partner">Brannock Electric</span>
    <span class="proof-sep"></span>
    <span class="stat">2K</span>
    <span class="stat-label">installed<br>chargers</span>
  </div>
</section>

<section>
  <h2 class="abs consult-title">EV CHARGER INSTALLATION CONSULTATION<br>AND UPGRADES</h2>
  <div class="abs consult-rule"></div>
  <svg class="abs" style="left:200px;top:1260px" width="800" height="330" viewBox="0 0 800 330">
    <g stroke="#e4e4e4" stroke-width="1" fill="none">
      <line x1="12" y1="138" x2="198" y2="138"/><line x1="198" y1="138" x2="306" y2="60"/>
      <line x1="582" y1="138" x2="788" y2="138"/><line x1="582" y1="138" x2="490" y2="60"/>
      <line x1="96" y1="320" x2="284" y2="320"/><line x1="284" y1="320" x2="352" y2="226"/>
      <line x1="520" y1="320" x2="720" y2="320"/><line x1="520" y1="320" x2="448" y2="226"/>
    </g>
    <circle cx="400" cy="125" r="113" fill="none" stroke="#7cc242" stroke-width="1.5" stroke-dasharray="2 4"/>
    <circle cx="400" cy="125" r="88" fill="#fff" stroke="#7cc242" stroke-width="6"/>
    <circle cx="306" cy="59" r="4" fill="#7cc242"/><circle cx="490" cy="59" r="4" fill="#7cc242"/>
    <circle cx="352" cy="226" r="4" fill="#7cc242"/><circle cx="448" cy="226" r="4" fill="#7cc242"/>
    <text x="400" y="136" text-anchor="middle" font-family="Roboto Condensed, sans-serif" font-weight="700" font-size="30" fill="#1b1b1b">VoltNest</text>
  </svg>
  <div class="abs step" style="left:210px;top:1287px">
    <div class="step-icon"><svg width="18" height="18" viewBox="0 0 24 24" fill="none" stroke="#7cc242" stroke-width="1.6"><rect x="5" y="3" width="12" height="17" rx="1"/><line x1="8" y1="8" x2="14" y2="8"/><line x1="8" y1="12" x2="12" y2="12"/><circle cx="16" cy="17" r="3"/></svg></div>
    Assessment of electrical system for safe and convenient charger placement.
  </div>
  <div class="abs step" style="left:781px;top:1287px">
    <div class="step-icon"><svg width="18" height="18" viewBox="0 0 24 24" fill="none" stroke="#7cc242" stroke-width="1.6"><path d="M4 14v-2a8 8 0 0 1 16 0v2"/><rect x="3" y="14" width="4" height="6" rx="1"/><rect x="17" y="14" width="4" height="6" rx="1"/></svg></div>
    Consultation and quote for necessary upgrades provided.
  </div>
  <div class="abs step" style="left:288px;top:1467px">
    <div class="step-icon"><svg width="18" height="18" viewBox="0 0 24 24" fill="none" stroke="#7cc242" stroke-width="1.6"><circle cx="12" cy="12" r="3"/><circle cx="12" cy="12" r="7" stroke-dasharray="3 2"/></svg></div>
    Possible upgrade required for electrical panel or Main electrical service system.
  </div>
  <div class="abs step" style="left:731px;top:1467px">
    <div class="step-icon"><svg width="18" height="18" viewBox="0 0 24 24" fill="none" stroke="#7cc242" stroke-width="1.6"><rect x="4" y="5" width="16" height="4"/><line x1="8" y1="12" x2="7" y2="19"/><line x1="12" y1="12" x2="11" y2="19"/><line x1="16" y1="12" x2="15" y2="19"/></svg></div>
    Smoke detectors may need updating to meet current code standards in some areas.
  </div>
</section>

<section>
  <div class="abs cost-left" role="img" aria-label="Green-tinted view of an EV plugged in to charge"></div>
  <div class="abs cost-photo" role="img" aria-label="Black wall charger with cable mounted on siding"></div>
  <div class="abs cost-copy">
    <h2>WHAT DOES THE INSTALLATION COST?</h2>
    <div class="rule"></div>
    <p>The cost of EV charger installation will vary depending on a number of factors, including the type of charger, the distance and access to the electrical panel.</p>
    <div class="price"><span class="price-icon">$</span><span>Typical charger installations range from<br>$600 to $2,000</span></div>
    <p class="after">Once your EV charger is installed, you'll start enjoying the convenience of athome/business charging and the many benefits of owning an EV.</p>
  </div>
  <p class="abs permit">VOLTNEST WILL ACQUIRE THE REQUIRED ELECTRICAL PERMIT FOR YOUR JOB</p>
</section>

<section>
  <div class="abs projects-bg"></div>
  <h2 class="abs projects-title">OUR FEATURED PROJECTS</h2>
  <div class="abs projects-rule"></div>
  <div class="abs project p1" role="img" aria-label="Garage wall charger beside a parked SUV"></div>
  <div class="abs project p2" role="img" aria-label="Charger on a green painted wall"></div>
  <div class="abs p2-overlay">
    <h4>SOLUTION FOR COMERCIAL</h4>
    <p>Lorem ipsum dolor sit amet consectetur. Neque iaculis tempus in dolor vulputate urna aliquam.</p>
  </div>
  <div class="abs project p3" role="img" aria-label="Open electrical panel with breakers"></div>
  <div class="abs project p4" role="img" aria-label="New service meter on a wooden wall"></div>
  <a class="abs arrow" href="#" style="left:71px" aria-label="Previous"><svg width="14" height="14" viewBox="0 0 24 24" fill="none" stroke="#333" stroke-width="2"><polyline points="15 5 8 12 15 19"/></svg></a>
  <a class="abs arrow" href="#" style="left:1080px" aria-label="Next"><svg width="14" height="14" viewBox="0 0 24 24" fill="none" stroke="#333" stroke-width="2"><polyline points="9 5 16 12 9 19"/></svg></a>
  <a class="abs btn-outline" href="#">VIEW ALL PROJECTS</a>
</section>

<section>
  <div class="abs cta" role="img" aria-label="Family beside a white EV charging at home"></div>
  <h2 class="abs cta-title">We Look Forward To Discussing Your EV Charger Installation Evaluation and Estimate</h2>
  <a class="abs btn-green" href="#">CONTACT VOLTNEST TODAY</a>
</section>

<footer class="abs site-footer"></footer>
<a class="abs brand footer-brand" href="#" style="left:143px;top:3202px">
  <span class="brand-mark"></span>
  <span><span class="brand-name">VoltNest</span><br><span class="brand-tag">EV CHARGER INSTALLATION</span></span>
</a>
<ul class="abs footer-nav" style="color:#fff"><li>HOME</li><li>JOB GALLERY</li><li>CONTACT US</li></ul>
<ul class="abs footer-contact">
  <li><svg width="11" height="11" viewBox="0 0 24 24"><path fill="#fff" d="M6.6 10.8a15 15 0 0 0 6.6 6.6l2.2-2.2a1 1 0 0 1 1-.25 11.4 11.4 0 0 0 3.6.57 1 1 0 0 1 1 1V20a1 1 0 0 1-1 1A17 17 0 0 1 3 4a1 1 0 0 1 1-1h3.5a1 1 0 0 1 1 1c0 1.25.2 2.45.57 3.57a1 1 0 0 1-.25 1z"/></svg>555 - 014 - 2290</li>
  <li><svg width="11" height="11" viewBox="0 0 24 24"><path fill="#fff" d="M12 2a7 7 0 0 0-7 7c0 5 7 13 7 13s7-8 7-13a7 7 0 0 0-7-7zm0 9.5A2.5 2.5 0 1 1 12 6.5a2.5 2.5 0 0 1 0 5z"/></svg><span>418 Linden Hollow Rd. Fairmont,<br>Illinois 62830</span></li>
  <li><svg width="11" height="11" viewBox="0 0 24 24"><rect x="2" y="5" width="20" height="14" fill="#fff"/><polyline points="2 5 12 13 22 5" fill="none" stroke="#222" stroke-width="2"/></svg>hello@voltnest.example</li>
</ul>
<p class="abs follow">Follow us</p>
<div class="abs socials"><span class="social"></span><span class="social"></span><span class="social"></span><span class="social"></span></div>
<p class="abs copyright" style="color:#fff">© Copyright 2023 VoltNest | All Rights Reserved</p>

</body>
</html>
```